Vantrelix Template Refresh 2017

We want software development managers to remember that presentations using this template showcased Vantrelix technology: Our template must be distinctive to be remembered as showing Vantrelix technology: They must stand out from the 100s of other tech presentations they see, without being 'wacky', but professional whether bold or subtle. We are targeting the world's largest corporations.

[What do we do?] Vantrelix offers the world's first objective, fair measure of software developer productivity (Vantrelix Keystroke Gauge) and code quality (Vantrelix DUX) metrics.

Our corporate colour is (hex) Red: 13, Green: 10, Blue: 74.

Target Market(s)

CIOs, CTOs and senior software development managers in large Enterprises.

Industry/Entity Type

Information Technology

Font styles to use
Sans Serif

Colors
0355a3

Requirements
Must have
• A memorable design
Nice to have
• Template for slides that will show a view of our User Interface (which shows graphs and charts); ideally a consistent theme to make it clear that this is our own UI, not general graphs and charts to illustrate the presentation. (None of the graphs and charts in the attached presentation are from our User Interface)
• A suggestion would be to make use of our "chord" shape (cut off circle in our logo). This could be white on a blue to appear as a cut-out window for the slide content.
Should not have
• A colourful / jokey / fun tone.

```html
<!DOCTYPE html>
<html lang="en">
<head>
<meta charset="utf-8">
<title>Calculating Coding Effort – Vantrelix</title>
<link rel="stylesheet" href="https://fonts.googleapis.com/css2?family=Arimo:wght@400;700&family=Roboto+Condensed:wght@700&family=Signika:wght@300&display=swap">
<style>
  :root {
    --navy: #0d0a4a;
    --navy-mid: #1b1a6b;
    --blue-deep: #1f2a80;
    --accent: #0355a3;
    --ink: #0d0a4a;
    --text: #12105a;
    --white: #ffffff;
  }
  * { box-sizing: border-box; margin: 0; padding: 0; }
  html, body { width: 1200px; height: 846px; overflow: hidden; background: var(--white); }
  .slide { position: relative; width: 1200px; height: 846px; overflow: hidden; background: var(--white); }

  .hero-backdrop {
    position: absolute; left: 0; top: 0; width: 1200px; height: 659px;
    background:
      radial-gradient(ellipse at 25% 30%, rgba(60,80,170,0.45), transparent 60%),
      linear-gradient(135deg, var(--navy-mid) 0%, var(--blue-deep) 45%, var(--navy) 100%);
  }
  .chord-window { position: absolute; left: 0; top: 0; width: 1200px; height: 659px; }

  .deck-title {
    position: absolute; left: 61px; top: 52px;
    font-family: "Signika", sans-serif; font-weight: 300;
    font-size: 38px; line-height: 46px; color: var(--white);
  }
  .topic-list {
    position: absolute; right: 48px; top: 130px; text-align: right;
    font-family: "Roboto Condensed", sans-serif; font-weight: 700;
    font-size: 25px; line-height: 34px; color: var(--ink);
  }
  .section-heading {
    position: absolute; left: 463px; top: 222px;
    font-family: "Signika", sans-serif; font-weight: 300;
    font-size: 48px; line-height: 56px; color: var(--ink);
  }
  .lead-copy {
    position: absolute; left: 471px; top: 294px; width: 705px;
    font-family: "Arimo", sans-serif; font-weight: 700;
    font-size: 15.3px; line-height: 21.5px; color: var(--text);
  }
  .body-copy {
    position: absolute; left: 471px; top: 446px; width: 470px;
    font-family: "Arimo", sans-serif; font-weight: 400;
    font-size: 15.3px; line-height: 22.5px; color: var(--text);
  }
  .process-diagram {
    position: absolute; left: 1043px; top: 446px; width: 134px; height: 126px;
    border-radius: 50%;
    background: radial-gradient(circle at 60% 60%, var(--navy) 0%, var(--accent) 45%, #7fb7d8 75%, rgba(255,255,255,0) 76%);
  }

  .footer-rule { position: absolute; left: 0; top: 659px; width: 1200px; height: 22px; background: var(--navy-mid); }
  .footer-copy {
    position: absolute; left: 29px; top: 698px; width: 590px;
    font-family: "Arimo", sans-serif; font-weight: 700;
    font-size: 15.3px; line-height: 22.5px; color: var(--navy);
  }
  .brand-name {
    position: absolute; right: 34px; top: 740px;
    font-family: "Arimo", sans-serif; font-weight: 700;
    font-size: 44px; line-height: 50px; letter-spacing: -1px; color: var(--navy);
  }
</style>
</head>
<body>
<main class="slide">
  <div class="hero-backdrop" role="img" aria-label="Dark blue photograph of source code on a screen"></div>
  <svg class="chord-window" viewBox="0 0 1200 659" aria-hidden="true">
    <circle cx="939" cy="895" r="838" fill="#ffffff"/>
  </svg>

  <h1 class="deck-title">Calculating Coding<br>Effort</h1>
  <p class="topic-list">How it works / Productivity /<br>DUX Quality / Architecture</p>

  <h2 class="section-heading">Lorem Ipsum,</h2>
  <p class="lead-copy">Lorem ipsum dolor sit amet, soleat vituperata scribentur per ne, has ea alia dolor. Labitur efficiantur ut per, sed labitur adipiscing no. Errem aeterno ne his, et dico reque nam. Tempor possim euismod cu per, alterum delicata constituto no nec, cu eos augue nulla dolorem. Nec ex omnium corpora delicata, et sit eius mutat. Alterum saperet philosophia vel ex, mel ei solum invenire intellegat, quis omnes concludaturque mei te</p>
  <p class="body-copy">Lorem ipsum dolor sit amet, soleat vituperata scribentur per ne, has ea alia dolor. Labitur efficiantur ut per, sed labitur adipiscing no. Errem aeterno ne his, et dico reque nam. Tempor possim euismod cu per, alterum delicata constituto no nec, cu eos augue nulla dolorem. Nec ex omnium corpora delicata, et sit eius mutat. Alterum saperet philosophia vel ex, mel ei solum invenire intellegat, quis omnes concludaturque mei te</p>
  <div class="process-diagram" role="img" aria-label="Illustration of three interlocking gears in blue tones representing the coding effort process"></div>

  <div class="footer-rule"></div>
  <p class="footer-copy">Lorem ipsum dolor sit amet, soleat vituperata scribentur per ne, has ea alia dolor. Labitur efficiantur ut per, sed labitur adipiscing no. Errem aeterno ne his, et dico reque nam. Tempor possim euismod cu per, alterum delicata constituto no nec, cu eos augue nulla dolorem. Nec ex omnium corpora delicata, et sit eius mutat. Alterum saperet philosophia vel ex, mel ei solum invenire intellegat, quis omnes</p>
  <p class="brand-name">Vantrelix</p>
</main>
</body>
</html>
```